Upbeat Accouting Package Flyer

I am looking for a 1 page (front, or front and back) flyer that will become our marketing for our accounting services. We are looking for something a little different and we are catering to the small retail shop owners. We have 3 accounting packages we would like to display and then some add-ons. I have included our logo that must be included in the design. I have uploaded the accounting package information as well.
Target Market(s)
Small Retail Shop Owners
Industry/Entity Type
Accounting
Colors
Designer to choose colors to be used in the design.
Requirements
Must have
- A casual feel. We are not your typical accountants who are very professional and "stuffy". I want it to feel like we are all family.
Nice to have
- I would like to incorporate some sort of retail theme.
- We have a couple of taglines we like to use and it would be great if they could be included. They are "We know you CAN do the accounting, but do you WANT to?" and "We allow you to get back to what's important."
Should not have
- Typical stock accounting photos of people shaking hands, large office buildings, etc.

```html
<!DOCTYPE html>
<html lang="en">
<head>
<meta charset="utf-8">
<title>Brightway Tax and Accounting – Accounting Packages Flyer</title>
<link href="https://fonts.googleapis.com/css2?family=Comfortaa:wght@400;700&family=Quicksand:wght@500;700&display=swap" rel="stylesheet">
<style>
  :root {
    --stage: #3a3a3a;
    --ink: #262626;
    --teal: #29b8d0;
    --teal-soft: rgba(41,184,208,0.55);
    --band: rgba(90,90,90,0.72);
    --white: #ffffff;
    --logo-bg: #1d1d1d;
  }
  * { margin: 0; padding: 0; box-sizing: border-box; }
  html, body { width: 1200px; height: 845px; overflow: hidden; background: var(--stage); }
  body { position: relative; font-family: "Quicksand", sans-serif; color: var(--ink); }

  .side-label {
    position: absolute; top: 14px; width: 579px; text-align: center;
    font-family: "Comfortaa", sans-serif; font-weight: 700; font-size: 34px; color: var(--white);
  }
  .side-label--front { left: 13px; }
  .side-label--back { left: 608px; }

  .panel { position: absolute; top: 77px; width: 579px; height: 749px; overflow: hidden; }
  .panel--front { left: 13px; }
  .panel--back { left: 608px; }

  .store-aisle {
    position: absolute; inset: 0;
    background:
      radial-gradient(ellipse 30% 45% at 78% 12%, rgba(255,255,255,0.9), transparent 70%),
      radial-gradient(ellipse 35% 40% at 60% 85%, #e6e6e2, transparent 70%),
      linear-gradient(100deg, #c9532e 0%, #e0a54a 18%, #d98a3c 32%, #cfc8bd 52%, #dcdad4 68%, #b9b4ad 85%, #d7c9b2 100%);
  }
  .store-aisle--faded::after {
    content: ""; position: absolute; inset: 0; background: rgba(255,255,255,0.8);
  }

  .brand-plate {
    position: absolute; left: 114px; top: 319px; width: 351px; height: 110px;
    background: var(--logo-bg); color: var(--white);
    display: flex; flex-direction: column; justify-content: center; padding-left: 22px;
  }
  .brand-name { font-family: "Comfortaa", sans-serif; font-weight: 700; font-size: 46px; line-height: 1; }
  .brand-sub { font-family: "Comfortaa", sans-serif; font-weight: 700; font-size: 13px; margin-top: 8px; letter-spacing: 0.5px; }

  .headline {
    position: absolute; left: 34px; top: 34px;
    font-family: "Comfortaa", sans-serif; font-weight: 400; font-size: 37px; line-height: 38px; color: var(--ink);
  }
  .headline .accent { color: var(--teal); }
  .headline .indent { padding-left: 54px; }

  .question-mark {
    position: absolute; left: 438px; top: 20px; width: 110px; height: 170px;
  }

  .packages-band {
    position: absolute; left: 0; top: 162px; width: 272px; height: 35px;
    background: var(--band); border-radius: 0 8px 8px 0;
    font-family: "Comfortaa", sans-serif; font-size: 19px; color: var(--teal);
    padding: 7px 0 0 34px;
  }

  .package {
    position: absolute; border: 2px solid var(--teal); border-top: none;
    border-radius: 0 0 16px 0; padding: 13px 10px 0 11px;
  }
  .package::before {
    content: ""; position: absolute; top: 0; left: -2px; width: 60%; height: 2px; background: var(--teal);
  }
  .package--develop { left: 36px; top: 221px; width: 236px; height: 181px; }
  .package--relax { left: 36px; top: 427px; width: 236px; height: 287px; }
  .package--grow { left: 308px; top: 221px; width: 236px; height: 275px; }
  .package--extras { left: 308px; top: 522px; width: 236px; height: 121px; }

  .package-title { font-family: "Comfortaa", sans-serif; font-size: 19px; font-weight: 400; margin-bottom: 9px; }
  .package-title small { font-size: 12px; }
  .feature-list { list-style: none; }
  .feature-list li {
    position: relative; font-size: 10.5px; line-height: 12px; padding-left: 13px; margin-bottom: 4.3px;
  }
  .feature-list li::before {
    content: ""; position: absolute; left: 1px; top: 3px; width: 5px; height: 5px; border-radius: 50%; background: var(--ink);
  }

  .package-icon { position: absolute; width: 52px; height: 52px; }
  .package-icon--develop { left: 212px; top: 204px; }
  .package-icon--relax { left: 212px; top: 408px; }
  .package-icon--grow { left: 484px; top: 204px; }

  .back-brand {
    position: absolute; left: 306px; top: 660px; width: 240px; color: var(--ink); text-align: right;
  }
  .back-brand .brand-name { font-size: 40px; }
  .back-brand .brand-sub { font-size: 11.5px; margin-top: 6px; }
</style>
</head>
<body>
  <div class="side-label side-label--front">front</div>
  <div class="side-label side-label--back">back</div>

  <section class="panel panel--front">
    <div class="store-aisle" role="img" aria-label="Blurred photo of a grocery store aisle with colourful shelves"></div>
    <div class="brand-plate">
      <div class="brand-name">brightway</div>
      <div class="brand-sub">TAX AND ACCOUNTING INC.</div>
    </div>
  </section>

  <section class="panel panel--back">
    <div class="store-aisle store-aisle--faded" role="img" aria-label="Faded blurred photo of a grocery store aisle"></div>

    <svg class="question-mark" viewBox="0 0 110 170" aria-hidden="true">
      <circle cx="42" cy="123" r="64" fill="var(--teal)" opacity="0.45"/>
      <text x="55" y="150" text-anchor="middle" font-family="Comfortaa, sans-serif" font-weight="700" font-size="190" fill="#262626">?</text>
    </svg>

    <h1 class="headline">
      <div>We know you <span class="accent">CAN</span></div>
      <div>do the accounting,</div>
      <div class="indent">but do you <span class="accent">WANT</span> to</div>
    </h1>

    <div class="packages-band">Accounting Packages:</div>

    <article class="package package--develop">
      <h2 class="package-title">Develop:</h2>
      <ul class="feature-list">
        <li>$300/mo when paid annually;<br>$325/mo billed monthly</li>
        <li>LedgerCloud Online subscription</li>
        <li>Free accounting setup</li>
        <li>Weekly transaction processing</li>
        <li>Monthly account reconciliation<br>(up to 2 accounts)</li>
        <li>Monthly financial statements by the<br>15th of the month</li>
      </ul>
    </article>

    <article class="package package--relax">
      <h2 class="package-title">Relax <small>(We've Got This):</small></h2>
      <ul class="feature-list">
        <li>$850/mo billed annually;<br>$875/mo billed monthly</li>
        <li>LedgerCloud Online subscription</li>
        <li>Free accounting setup</li>
        <li>Weekly transaction processing</li>
        <li>Monthly account reconciliation<br>(up to 5-10 accounts)</li>
        <li>Monthly financial statements<br>by the 5th of the month</li>
        <li>Client portal access for document<br>sharing</li>
        <li>2 Custom Reports</li>
        <li>Accounts Payable</li>
        <li>Invoicing and accounts receivable</li>
        <li>Weekly Scorecard (customized metric<br>tracking for your business)</li>
      </ul>
    </article>

    <article class="package package--grow">
      <h2 class="package-title">Grow:</h2>
      <ul class="feature-list">
        <li>$550/mo billed annually;<br>$575/mo billed monthly</li>
        <li>LedgerCloud Online subscription</li>
        <li>Free accounting setup</li>
        <li>Weekly transaction processing</li>
        <li>Monthly account reconciliation<br>(up to 4 accounts)</li>
        <li>Monthly financial statements by the<br>10th of the month</li>
        <li>Client portal access for document<br>sharing</li>
        <li>1 Custom Report</li>
        <li>Accounts Payable</li>
        <li>Monthly Scorecard (customized<br>metric tracking for your business)</li>
      </ul>
    </article>

    <article class="package package--extras">
      <h2 class="package-title">Additional Options</h2>
      <ul class="feature-list">
        <li>Payroll – 1-10 employees $85/mo;<br>11-30 employees $175/mo</li>
        <li>Sales tax - $30/mo per state</li>
        <li>Corporate taxes $50/mo</li>
        <li>Owner taxes - $25/mo</li>
      </ul>
    </article>

    <svg class="package-icon package-icon--develop" viewBox="0 0 52 52" aria-hidden="true">
      <circle cx="26" cy="26" r="26" fill="var(--teal)"/>
      <circle cx="22" cy="28" r="9" fill="none" stroke="#fff" stroke-width="4"/>
      <line x1="27" y1="23" x2="40" y2="10" stroke="#fff" stroke-width="5" stroke-linecap="round"/>
    </svg>
    <svg class="package-icon package-icon--relax" viewBox="0 0 52 52" aria-hidden="true">
      <circle cx="26" cy="26" r="26" fill="var(--teal)"/>
      <path d="M11 34 Q26 24 41 34" fill="none" stroke="#fff" stroke-width="4" stroke-linecap="round"/>
      <line x1="14" y1="40" x2="38" y2="40" stroke="#fff" stroke-width="3" stroke-linecap="round"/>
    </svg>
    <svg class="package-icon package-icon--grow" viewBox="0 0 52 52" aria-hidden="true">
      <circle cx="26" cy="26" r="26" fill="var(--teal)"/>
      <path d="M26 34 V20 M26 24 Q18 22 17 14 Q25 15 26 24 M26 22 Q33 19 35 12 Q27 12 26 22" fill="#fff" stroke="#fff" stroke-width="2"/>
      <path d="M12 34 Q26 42 40 34" fill="none" stroke="#fff" stroke-width="4" stroke-linecap="round"/>
    </svg>

    <div class="back-brand">
      <div class="brand-name">brightway</div>
      <div class="brand-sub">TAX AND ACCOUNTING INC.</div>
    </div>
  </section>
</body>
</html>
```